Team email banner for internal communications

We need a team email banner/header that will be applied to all internal communications from our department to other functions. The graphic should be optimized for Outlook and be landscape in layout. We have 5 different silo within our team and will need so will either need have a blank space to denote each team or have change in colors/graphics to denote each team (see current headers attached to job description). We are looking for a banner that combines our team logo (attached) with our team name, Regional Talent & Coaching Unit. The theme should be L&D and pharmaceutical in nature.

Need extra days to review

The text in the banner should be Regional Talent & Coaching Unit with the team logo (attached).

```html
<!DOCTYPE html>
<html lang="en">
<head>
<meta charset="utf-8">
<title>Regional Talent &amp; Coaching Unit – Team Email Banners</title>
<link rel="stylesheet" href="https://fonts.googleapis.com/css2?family=Hind:wght@600&family=Montserrat:wght@400;700&display=swap">
<style>
  :root {
    --page: #ffffff;
    --panel: #f1f1f1;
    --ink: #333333;
    --slate: #616161;
    --ring: #c9ced8;
    --rule: #d62a22;
    --hematology: #ff5468;
    --solid-tumor: #6a67cd;
    --leadership: #33c18f;
    --market-access: #fda12e;
    --operations: #3599cf;
  }
  html, body {
    margin: 0;
    padding: 0;
    overflow: hidden;
    background: var(--page);
  }
  .canvas {
    position: relative;
    width: 720px;
    height: 1200px;
    overflow: hidden;
    background: var(--page);
  }
  .banner {
    position: absolute;
    left: 54px;
    width: 612px;
    height: 204px;
    display: block;
  }
  .banner--hematology   { top: 18px;  --accent: var(--hematology); }
  .banner--solid-tumor  { top: 258px; --accent: var(--solid-tumor); }
  .banner--leadership   { top: 498px; --accent: var(--leadership); }
  .banner--market       { top: 738px; --accent: var(--market-access); }
  .banner--operations   { top: 978px; --accent: var(--operations); }

  .panel    { fill: var(--panel); }
  .accent   { fill: var(--accent); }
  .slate    { fill: var(--slate); }
  .badge-ring  { fill: var(--panel); stroke: var(--ring); stroke-width: 8; }
  .badge-core  { fill: #ffffff; stroke: var(--accent); stroke-width: 5; }
  .chevron  { fill: none; stroke: var(--ring); stroke-width: 6; stroke-linejoin: round; }
  .rule     { stroke: var(--rule); stroke-width: 4; }
  .badge-name {
    font-family: "Montserrat", sans-serif;
    font-weight: 700;
    font-size: 36px;
    fill: var(--ink);
  }
  .silo-label {
    font-family: "Hind", sans-serif;
    font-weight: 600;
    font-size: 31px;
    fill: #ffffff;
  }
  .team-name {
    font-family: "Montserrat", sans-serif;
    font-weight: 700;
    font-size: 56px;
    letter-spacing: 4px;
    fill: var(--ink);
  }
  .team-sub {
    font-family: "Montserrat", sans-serif;
    font-weight: 400;
    font-size: 19px;
    fill: var(--ink);
  }
</style>
</head>
<body>
<main class="canvas">

  <svg class="banner banner--hematology" viewBox="0 0 1020 340" role="group" aria-label="Hematology banner">
    <rect class="panel" width="1020" height="340"/>
    <rect class="accent" width="138" height="340"/>
    <polygon class="accent" points="715,0 800,0 812,20 730,20"/>
    <polygon class="slate" points="795,0 1020,0 1020,40 826,40"/>
    <polygon class="slate" points="533,305 680,305 660,340 510,340"/>
    <path class="accent" d="M648,340 L692,280 Q700,270 714,270 H1020 V340 Z"/>
    <circle class="accent" cx="138" cy="170" r="112"/>
    <polyline class="chevron" points="476,112 498,112 538,170 498,228 476,228"/>
    <path class="accent" d="M200,100 H452 Q464,100 471,110 L506,160 Q513,170 506,180 L471,230 Q464,240 452,240 H200 Z"/>
    <circle class="badge-ring" cx="138" cy="170" r="90"/>
    <circle class="badge-core" cx="138" cy="170" r="72"/>
    <text class="badge-name" x="138" y="183" text-anchor="middle">RTC</text>
    <text class="silo-label" x="226" y="180">HEMATOLOGY</text>
    <text class="team-name" x="565" y="178" textLength="405">REGIONAL</text>
    <line class="rule" x1="565" y1="196" x2="618" y2="196"/>
    <text class="team-sub" x="767" y="203" text-anchor="middle">TALENT &amp; COACHING UNIT</text>
    <line class="rule" x1="916" y1="196" x2="970" y2="196"/>
  </svg>

  <svg class="banner banner--solid-tumor" viewBox="0 0 1020 340" role="group" aria-label="Solid tumor banner">
    <rect class="panel" width="1020" height="340"/>
    <rect class="accent" width="138" height="340"/>
    <polygon class="accent" points="715,0 800,0 812,20 730,20"/>
    <polygon class="slate" points="795,0 1020,0 1020,40 826,40"/>
    <polygon class="slate" points="533,305 680,305 660,340 510,340"/>
    <path class="accent" d="M648,340 L692,280 Q700,270 714,270 H1020 V340 Z"/>
    <circle class="accent" cx="138" cy="170" r="112"/>
    <polyline class="chevron" points="476,112 498,112 538,170 498,228 476,228"/>
    <path class="accent" d="M200,100 H452 Q464,100 471,110 L506,160 Q513,170 506,180 L471,230 Q464,240 452,240 H200 Z"/>
    <circle class="badge-ring" cx="138" cy="170" r="90"/>
    <circle class="badge-core" cx="138" cy="170" r="72"/>
    <text class="badge-name" x="138" y="183" text-anchor="middle">RTC</text>
    <text class="silo-label" x="226" y="180">SOLID TUMOR</text>
    <text class="team-name" x="565" y="178" textLength="405">REGIONAL</text>
    <line class="rule" x1="565" y1="196" x2="618" y2="196"/>
    <text class="team-sub" x="767" y="203" text-anchor="middle">TALENT &amp; COACHING UNIT</text>
    <line class="rule" x1="916" y1="196" x2="970" y2="196"/>
  </svg>

  <svg class="banner banner--leadership" viewBox="0 0 1020 340" role="group" aria-label="Leadership development banner">
    <rect class="panel" width="1020" height="340"/>
    <rect class="accent" width="138" height="340"/>
    <polygon class="accent" points="715,0 800,0 812,20 730,20"/>
    <polygon class="slate" points="795,0 1020,0 1020,40 826,40"/>
    <polygon class="slate" points="533,305 680,305 660,340 510,340"/>
    <path class="accent" d="M648,340 L692,280 Q700,270 714,270 H1020 V340 Z"/>
    <circle class="accent" cx="138" cy="170" r="112"/>
    <polyline class="chevron" points="476,112 498,112 538,170 498,228 476,228"/>
    <path class="accent" d="M200,100 H452 Q464,100 471,110 L506,160 Q513,170 506,180 L471,230 Q464,240 452,240 H200 Z"/>
    <circle class="badge-ring" cx="138" cy="170" r="90"/>
    <circle class="badge-core" cx="138" cy="170" r="72"/>
    <text class="badge-name" x="138" y="183" text-anchor="middle">RTC</text>
    <text class="silo-label" x="226" y="160">LEADERSHIP</text>
    <text class="silo-label" x="226" y="198">DEVELOPMENT</text>
    <text class="team-name" x="565" y="178" textLength="405">REGIONAL</text>
    <line class="rule" x1="565" y1="196" x2="618" y2="196"/>
    <text class="team-sub" x="767" y="203" text-anchor="middle">TALENT &amp; COACHING UNIT</text>
    <line class="rule" x1="916" y1="196" x2="970" y2="196"/>
  </svg>

  <svg class="banner banner--market" viewBox="0 0 1020 340" role="group" aria-label="Market access banner">
    <rect class="panel" width="1020" height="340"/>
    <rect class="accent" width="138" height="340"/>
    <polygon class="accent" points="715,0 800,0 812,20 730,20"/>
    <polygon class="slate" points="795,0 1020,0 1020,40 826,40"/>
    <polygon class="slate" points="533,305 680,305 660,340 510,340"/>
    <path class="accent" d="M648,340 L692,280 Q700,270 714,270 H1020 V340 Z"/>
    <circle class="accent" cx="138" cy="170" r="112"/>
    <polyline class="chevron" points="476,112 498,112 538,170 498,228 476,228"/>
    <path class="accent" d="M200,100 H452 Q464,100 471,110 L506,160 Q513,170 506,180 L471,230 Q464,240 452,240 H200 Z"/>
    <circle class="badge-ring" cx="138" cy="170" r="90"/>
    <circle class="badge-core" cx="138" cy="170" r="72"/>
    <text class="badge-name" x="138" y="183" text-anchor="middle">RTC</text>
    <text class="silo-label" x="226" y="180">MARKET ACCESS</text>
    <text class="team-name" x="565" y="178" textLength="405">REGIONAL</text>
    <line class="rule" x1="565" y1="196" x2="618" y2="196"/>
    <text class="team-sub" x="767" y="203" text-anchor="middle">TALENT &amp; COACHING UNIT</text>
    <line class="rule" x1="916" y1="196" x2="970" y2="196"/>
  </svg>

  <svg class="banner banner--operations" viewBox="0 0 1020 340" role="group" aria-label="Operations and capabilities banner">
    <rect class="panel" width="1020" height="340"/>
    <rect class="accent" width="138" height="340"/>
    <polygon class="accent" points="715,0 800,0 812,20 730,20"/>
    <polygon class="slate" points="795,0 1020,0 1020,40 826,40"/>
    <polygon class="slate" points="533,305 680,305 660,340 510,340"/>
    <path class="accent" d="M648,340 L692,280 Q700,270 714,270 H1020 V340 Z"/>
    <circle class="accent" cx="138" cy="170" r="112"/>
    <polyline class="chevron" points="476,112 498,112 538,170 498,228 476,228"/>
    <path class="accent" d="M200,100 H452 Q464,100 471,110 L506,160 Q513,170 506,180 L471,230 Q464,240 452,240 H200 Z"/>
    <circle class="badge-ring" cx="138" cy="170" r="90"/>
    <circle class="badge-core" cx="138" cy="170" r="72"/>
    <text class="badge-name" x="138" y="183" text-anchor="middle">RTC</text>
    <text class="silo-label" x="226" y="160">OPERATIONS &amp;</text>
    <text class="silo-label" x="226" y="198">CAPABILITIES</text>
    <text class="team-name" x="565" y="178" textLength="405">REGIONAL</text>
    <line class="rule" x1="565" y1="196" x2="618" y2="196"/>
    <text class="team-sub" x="767" y="203" text-anchor="middle">TALENT &amp; COACHING UNIT</text>
    <line class="rule" x1="916" y1="196" x2="970" y2="196"/>
  </svg>

</main>
</body>
</html>
```